Business Card Design

We sell fish products to corporate food companies who then turn these products into final food products for consumers

Industry/Entity Type

Business

Contact Information for Business Card

I need a corporate business card template for a fish products business. We would like it be professional for use in dealing with multi national companies. This company business card template will be used by multiple employees so the following fields must be open to edit (Name, Phone Number and Email address)

```html
<!DOCTYPE html>
<html lang="en">
<head>
<meta charset="utf-8">
<title>Tidewater Seafoods – Business Card</title>
<link rel="stylesheet" href="https://fonts.googleapis.com/css2?family=Open+Sans:wght@400;600;700;800&display=swap">
<style>
  :root {
    --backdrop: #e4e4e2;
    --card: #ffffff;
    --brand-blue: #1a4fa0;
    --brand-green: #4dbb7f;
    --ink: #2b2b2b;
    --icon: #1a4fa0;
  }
  * { box-sizing: border-box; margin: 0; padding: 0; }
  html, body {
    width: 1200px;
    height: 800px;
    overflow: hidden;
    background: var(--backdrop);
    font-family: "Open Sans", Arial, sans-serif;
  }
  .stage {
    width: 1200px;
    height: 800px;
    display: flex;
    align-items: center;
    justify-content: center;
  }
  .business-card {
    position: relative;
    width: 700px;
    height: 400px;
    background: var(--card);
    box-shadow: 0 4px 18px rgba(0, 0, 0, 0.12);
  }
  .brand {
    position: absolute;
    top: 46px;
    left: 56px;
    display: flex;
    align-items: center;
    gap: 12px;
  }
  .brand-mark {
    width: 22px;
    height: 22px;
    border-radius: 50%;
    background: var(--brand-blue);
  }
  .brand-name {
    font-weight: 700;
    font-size: 30px;
    letter-spacing: 0.5px;
    color: var(--brand-blue);
  }
  .contact-list {
    position: absolute;
    top: 112px;
    left: 60px;
    list-style: none;
  }
  .contact-item {
    display: flex;
    align-items: center;
    gap: 14px;
    font-size: 15px;
    color: var(--ink);
    line-height: 26px;
  }
  .contact-icon {
    width: 14px;
    height: 14px;
    flex: none;
  }
  .person {
    position: absolute;
    right: 56px;
    bottom: 60px;
    text-align: right;
  }
  .person-name {
    font-weight: 800;
    font-size: 30px;
    letter-spacing: 0.3px;
  }
  .person-name .first { color: var(--brand-blue); }
  .person-name .last { color: var(--brand-green); }
  .person-title {
    font-size: 17px;
    color: var(--ink);
    margin-top: 2px;
  }
</style>
</head>
<body>
<main class="stage">
  <article class="business-card">
    <header class="brand">
      <span class="brand-mark" aria-hidden="true"></span>
      <span class="brand-name">TIDEWATER SEAFOODS</span>
    </header>

    <ul class="contact-list">
      <li class="contact-item">
        <svg class="contact-icon" viewBox="0 0 14 14" aria-hidden="true">
          <rect width="14" height="14" rx="2" fill="var(--icon)"/>
          <path d="M4 3.2c.4-.3.9-.2 1.1.2l.7 1.3c.2.3.1.7-.2.9l-.5.4c.4.9 1.1 1.6 2 2l.4-.5c.2-.3.6-.4.9-.2l1.3.7c.4.2.5.7.2 1.1l-.6.7c-.4.4-1 .5-1.5.3C5.9 9.3 4.7 8.1 3.9 6.3c-.2-.5-.1-1.1.3-1.5z" fill="#fff"/>
        </svg>
        <span>(555) 0148-0011</span>
      </li>
      <li class="contact-item">
        <svg class="contact-icon" viewBox="0 0 14 14" aria-hidden="true">
          <rect x="3" y="1" width="8" height="12" rx="1.5" fill="none" stroke="var(--icon)" stroke-width="1.4"/>
          <circle cx="7" cy="10.8" r="0.8" fill="var(--icon)"/>
        </svg>
        <span>(555)-0172-0125</span>
      </li>
      <li class="contact-item">
        <svg class="contact-icon" viewBox="0 0 14 14" aria-hidden="true">
          <rect y="2" width="14" height="10" rx="1.5" fill="var(--icon)"/>
          <path d="M1.5 3.5 7 8l5.5-4.5" fill="none" stroke="#fff" stroke-width="1.2"/>
        </svg>
        <span>marten@tidewaterseafoods.com</span>
      </li>
      <li class="contact-item">
        <svg class="contact-icon" viewBox="0 0 14 14" aria-hidden="true">
          <circle cx="7" cy="7" r="6.3" fill="var(--icon)"/>
          <ellipse cx="7" cy="7" rx="2.6" ry="6.3" fill="none" stroke="#fff" stroke-width="1"/>
          <path d="M0.8 7h12.4M2 4h10M2 10h10" stroke="#fff" stroke-width="0.9"/>
        </svg>
        <span>www.tidewaterseafoods.com</span>
      </li>
    </ul>

    <footer class="person">
      <p class="person-name"><span class="first">Marten</span> <span class="last">Dahl</span></p>
      <p class="person-title">Director</p>
    </footer>
  </article>
</main>
</body>
</html>
```